Wix Website Refresh and Redesign

Looking to update and refresh my Wix site. Psychotherapist specializing in treating Anxiety and OCD. Need something warm, professional, and inviting. Nothing super fancy, but needs to look well-designed and professional. I would also like a logo for my business Quiet Harbor. I would like the logo worked into the design.

```html
<!DOCTYPE html>
<html lang="en">
<head>
<meta charset="utf-8">
<title>Quiet Harbor – Anxiety and OCD Therapy Denver</title>
<link href="https://fonts.googleapis.com/css2?family=Open+Sans:wght@400;600;700&family=Roboto:wght@400;500;700&display=swap" rel="stylesheet">
<style>
:root{
  --sage:#9fb5ae;
  --ink:#1f1f1f;
  --charcoal:#3a3a3a;
  --text:#555;
  --muted:#777;
  --light:#eeeeef;
  --white:#fff;
}
*{box-sizing:border-box;margin:0;padding:0}
html,body{width:1200px;height:3958px;overflow:hidden}
body{font-family:'Roboto',sans-serif;color:var(--ink);background:var(--white);position:relative}
.heading{font-family:'Open Sans',sans-serif}
.accent{color:var(--sage)}
.rule{position:absolute;height:4px;background:var(--charcoal);border-radius:2px}
.btn{position:absolute;display:flex;align-items:center;justify-content:center;gap:8px;border-radius:24px;font-weight:700;color:var(--white);font-size:15px}
.btn .dot{width:14px;height:14px;border-radius:50%;background:var(--white);display:inline-flex;align-items:center;justify-content:center}
.btn .dot::after{content:"";border-left:5px solid var(--sage);border-top:3.5px solid transparent;border-bottom:3.5px solid transparent;margin-left:1px}
.btn.dark .dot::after{border-left-color:var(--charcoal)}

/* header + hero */
.hero{position:absolute;left:0;top:0;width:1200px;height:645px;background:linear-gradient(90deg,#ececec 0%,#f1f1f1 40%,#e4e4e4 60%,#d9d9d9 100%)}
.hero-photo{position:absolute;left:560px;top:0;width:640px;height:645px;background:linear-gradient(120deg,rgba(236,236,236,0) 0%,#d8d2c8 25%,#c9b98a 55%,#6f8eab 80%,#3b4b66 100%);opacity:.85}
.brand{position:absolute;left:144px;top:16px;display:flex;align-items:center;gap:10px}
.brand-mark{width:40px;height:40px;border-radius:50%;background:var(--sage)}
.brand-text{font-size:12px;line-height:17px;color:var(--ink)}
.brand-text b{font-weight:400;color:var(--sage)}
.nav{position:absolute;top:28px;font-size:14px;font-weight:500}
.nav.active::after{content:"";position:absolute;left:0;right:0;top:23px;height:2px;background:var(--sage)}
.login{left:951px;top:15px;width:103px;height:42px;border-radius:21px;background:var(--sage);font-size:14px;font-weight:500}
.hero-title{position:absolute;left:143px;top:162px;font-size:37px;line-height:50px;font-weight:700;color:var(--charcoal)}
.hero-lead{position:absolute;left:143px;top:324px;width:400px;font-size:16px;line-height:25px;color:var(--ink)}

/* therapy section */
.sec-title{position:absolute;left:0;width:1200px;text-align:center;font-size:33px;font-weight:700;color:var(--ink)}
.intro{position:absolute;left:148px;top:812px;width:904px;text-align:center;font-size:13px;line-height:23px;color:var(--text)}
.tab{position:absolute;top:931px;height:46px;border:2px solid var(--sage);border-radius:23px;display:flex;align-items:center;font-weight:700;font-size:16px}
.tab .num{width:46px;height:46px;border-radius:50%;background:var(--charcoal);color:var(--white);display:flex;align-items:center;justify-content:center;font-size:20px;margin-left:-2px;margin-right:16px}
.tab.on{background:var(--sage);color:var(--white)}
.card{position:absolute;top:1032px;width:287px;height:363px;background:var(--white);border-radius:0 60px 0 60px;box-shadow:0 4px 14px rgba(0,0,0,.1);overflow:hidden;text-align:center}
.card .photo{height:194px;background:linear-gradient(135deg,#c9c4bd,#8d8a86)}
.card .photo.dark{background:linear-gradient(135deg,#4a3a2c,#2a2420)}
.card .photo.room{background:linear-gradient(135deg,#b9b5b0,#6d625a)}
.card .icon{position:absolute;left:113px;top:161px;width:62px;height:62px;border-radius:50%;background:var(--charcoal);border:4px solid var(--white)}
.card .icon.sage{background:var(--sage)}
.card h3{font-family:'Roboto',sans-serif;font-size:20px;font-weight:500;margin-top:44px}
.card p{font-size:12.5px;line-height:20px;color:var(--muted);margin:10px 26px 0}
.card .more{display:inline-block;margin-top:10px;font-size:12px;font-weight:700;text-decoration:underline;color:var(--charcoal)}
.card .more.sage{color:var(--sage)}
.arrow{position:absolute;top:1210px;width:38px;height:38px;border-radius:50%;background:var(--charcoal)}

/* video + band */
.band-shape{position:absolute;left:0;top:1760px;width:1200px;height:614px}
.video{position:absolute;left:253px;top:1570px;width:693px;height:361px;border-radius:10px;background:#000;overflow:hidden}
.video .frame{position:absolute;left:165px;top:0;width:363px;height:361px;background:linear-gradient(160deg,#c8a772,#7d8ea8 60%,#465773)}
.video .play{position:absolute;left:321px;top:155px;width:52px;height:52px;border-radius:50%;background:rgba(255,255,255,.9)}
.video .play::after{content:"";position:absolute;left:20px;top:16px;border-left:16px solid var(--charcoal);border-top:10px solid transparent;border-bottom:10px solid transparent}
.video .title{position:absolute;left:64px;top:16px;color:#fff;font-size:12px}
.video .bar{position:absolute;left:34px;right:34px;bottom:26px;height:3px;background:rgba(255,255,255,.4)}
.band-title{position:absolute;left:0;top:1980px;width:1200px;text-align:center;color:var(--white);font-size:31px;line-height:52px;font-weight:700}
.band-copy{position:absolute;left:148px;top:2113px;width:904px;text-align:center;color:var(--white);font-size:13px;line-height:20px}
.band-copy p+p{margin-top:11px}

/* about */
.about-shadow{position:absolute;left:124px;top:2527px;width:300px;height:315px;background:var(--charcoal)}
.about-photo{position:absolute;left:143px;top:2455px;width:415px;height:368px;border-radius:0 44px 0 0;background:linear-gradient(160deg,#8e8a6e,#6d6a5b 45%,#3d5a8c 80%,#2d4878)}
.about-name{position:absolute;left:614px;top:2468px;font-size:33px;font-weight:700}
.about-copy{position:absolute;left:617px;top:2557px;width:438px;font-size:13px;line-height:24px;color:var(--text);text-align:justify}
.about-copy p+p{margin-top:10px}

/* contact */
.contact{position:absolute;left:0;top:2923px;width:1200px;height:748px;background:var(--light)}
.info{position:absolute;top:3072px;display:flex;gap:16px;align-items:flex-start}
.info b{display:block;font-size:15px;font-weight:700;margin-bottom:3px}
.info span{font-size:13px;color:var(--text);line-height:19px}
.lead{position:absolute;left:144px;top:3173px;width:450px;font-size:17px;line-height:28px}
.field{position:absolute;left:144px;width:431px;height:41px;background:var(--white);border:1px solid #ddd;border-radius:3px;font-size:11px;color:#666;padding:12px 0 0 21px}
.submit{position:absolute;left:144px;top:3552px;width:431px;height:41px;background:var(--sage);color:var(--white);font-weight:700;font-size:15px;display:flex;align-items:center;justify-content:center;border-radius:2px}
.map{position:absolute;left:634px;top:3176px;width:420px;height:415px;border:4px solid var(--white);background:linear-gradient(135deg,#e9efe6,#dde6ee 50%,#eae8e2)}

/* footer */
.footer{position:absolute;left:0;top:3671px;width:1200px;height:287px;background:linear-gradient(180deg,#444446,#363638)}
.foot-brand{position:absolute;left:484px;top:3720px;display:flex;align-items:center;gap:18px}
.foot-brand .brand-mark{width:64px;height:64px}
.foot-brand .t{font-family:'Open Sans',sans-serif;color:var(--white);font-size:20px;line-height:32px}
.foot-brand .t b{font-weight:400;color:var(--sage)}
.foot-nav{position:absolute;left:0;top:3802px;width:1200px;display:flex;justify-content:center;gap:30px;color:var(--white);font-size:14px;font-weight:500}
.copy{position:absolute;left:0;top:3843px;width:1200px;text-align:center;color:var(--white);font-size:12px}
.copy u{font-weight:500}
.socials{position:absolute;left:510px;top:3887px;display:flex;gap:10px}
.socials span{width:39px;height:39px;border-radius:50%;background:var(--white);display:flex;align-items:center;justify-content:center}
.socials span:first-child{background:var(--sage)}
.socials span::after{content:"";width:10px;height:10px;border-radius:50%;background:var(--charcoal)}
.socials span:first-child::after{background:var(--white)}
</style>
</head>
<body>

<!-- Header and hero -->
<section class="hero">
  <div class="hero-photo" role="img" aria-label="Photo of a therapist listening to an older client in a bright office"></div>
  <div class="brand"><span class="brand-mark"></span><div class="brand-text"><b>Quiet Harbor</b><br>Daniel Mercer,LCSW</div></div>
  <span class="nav active" style="left:365px">Home</span>
  <span class="nav" style="left:432px">Therapy</span>
  <span class="nav" style="left:513px">OCD</span>
  <span class="nav" style="left:571px">Anxiety Disorders</span>
  <span class="nav" style="left:712px">About Daniel</span>
  <span class="nav" style="left:822px">Contact</span>
  <span class="nav" style="left:898px">Blog</span>
  <div class="btn login">
    <svg width="11" height="12" viewBox="0 0 11 12"><rect x="1" y="5" width="9" height="7" rx="1" fill="#fff"/><path d="M3 5V3.5a2.5 2.5 0 0 1 5 0V5" stroke="#fff" stroke-width="1.5" fill="none"/></svg>Login</div>
  <h1 class="hero-title heading"><span class="accent">EVIDENCE</span>-BASED <span class="accent">ANXIETY</span><br>AND OCD <span class="accent">TREATMENT</span><br>DENVER, COLORADO</h1>
  <p class="hero-lead">Living with OCD or Anxiety can feel like navigating an endless maze with no real exit.</p>
  <div class="btn" style="left:143px;top:408px;width:347px;height:45px;background:var(--sage)">Schedule a Free Online Consultation <span class="dot"></span></div>
</section>

<!-- Therapy services -->
<h2 class="sec-title heading" style="top:721px">ANXIETY <span class="accent">THERAPY</span> DENVER, COLORADO</h2>
<div class="rule" style="left:474px;top:779px;width:252px"></div>
<p class="intro">I differ from a general therapist in that I specialize in only a few select disorders and treatments. I have spent the last decade exclusively studying and treating OCD and Anxiety. What does this mean for you? You get expert, evidence-based therapy from a therapist experienced in all aspects of these disorders.</p>

<div class="tab" style="left:72px;width:389px"><span class="num">01</span>Obsessive Compulsive Disorder (OCD)</div>
<div class="tab on" style="left:502px;width:294px"><span class="num">02</span>Anxiety Disorder Therapy</div>
<div class="tab" style="left:834px;width:295px"><span class="num">03</span>Anxiety Disorder Therapy</div>

<div class="arrow" style="left:73px"><svg width="38" height="38"><path d="M22 12l-7 7 7 7" stroke="#fff" stroke-width="2" fill="none"/></svg></div>
<div class="arrow" style="left:1089px"><svg width="38" height="38"><path d="M16 12l7 7-7 7" stroke="#fff" stroke-width="2" fill="none"/></svg></div>

<article class="card" style="left:146px">
  <div class="photo" role="img" aria-label="Photo of a young woman standing apart from a group of friends"></div>
  <span class="icon"></span>
  <h3>Social Anxiety</h3>
  <p>Lorem ipsum dolor sit amet, consectetur adipiscing elit, eiusmod aliqua.</p>
  <span class="more">LEARN MORE ➜</span>
</article>
<article class="card" style="left:456px">
  <div class="photo dark" role="img" aria-label="Photo of a woman meditating in a calm candle-lit room"></div>
  <span class="icon sage"></span>
  <h3>Healthy Anxiety</h3>
  <p>Lorem ipsum dolor sit amet, consectetur adipiscing elit, eiusmod aliqua.</p>
  <span class="more sage">LEARN MORE ➜</span>
</article>
<article class="card" style="left:765px">
  <div class="photo room" role="img" aria-label="Photo of a distressed woman holding her head on a sofa"></div>
  <span class="icon"></span>
  <h3>Panic Attacks</h3>
  <p>Lorem ipsum dolor sit amet, consectetur adipiscing elit, eiusmod aliqua.</p>
  <span class="more">LEARN MORE ➜</span>
</article>

<!-- Introduction video and message band -->
<h2 class="sec-title heading" style="top:1465px">DANIEL MERCER INTRODUCTION</h2>
<div class="rule" style="left:476px;top:1523px;width:248px"></div>

<svg class="band-shape" width="1200" height="614" viewBox="0 0 1200 614" role="img" aria-label="Soft sage band with a faint photo of a relaxed person">
  <defs><linearGradient id="bandFill" x1="0" y1="0" x2="1" y2="1"><stop offset="0" stop-color="#a6bab3"/><stop offset=".6" stop-color="#9bb1a9"/><stop offset="1" stop-color="#a9bcb5"/></linearGradient></defs>
  <path d="M0 84 Q600 -60 1200 84 V614 H0 Z" fill="url(#bandFill)"/>
</svg>

<div class="video" role="img" aria-label="Introduction video still of the therapist waving hello">
  <div class="frame"></div>
  <span class="title">Daniel Mercer, introduction</span>
  <span class="play"></span>
  <span class="bar"></span>
</div>

<h2 class="band-title heading">EVIDENCE-BASED ANXIETY<br>AND OCD TREATMENT - DENVER, COLORADO</h2>
<div class="band-copy">
  <p>Maybe you're here because you're wrestling with the challenges of OCD or Anxiety. Or maybe, you're here because you're worried about a friend or a loved one. Whatever the reason, I'm glad you're here. And here's what's most important to know: with the right evidence-based therapy, freedom from OCD and Anxiety isn't just possible—it's likely.</p>
  <p>Living with OCD or Anxiety can feel like navigating an endless maze with no real exit. You're trapped in a cycle of persistent worry and intrusive thoughts, like being caught in a relentless storm of 'what ifs.' If you're like many of my clients, you have tried various strategies but nothing seems to work. You may have even tried therapy before. But despite your best efforts, it feels like you can't get any real relief.</p>
</div>
<div class="btn dark" style="left:426px;top:2273px;width:347px;height:45px;background:var(--charcoal)">Schedule a Free Online Consultation <span class="dot"></span></div>

<!-- About -->
<section class="about">
  <div class="about-shadow"></div>
  <div class="about-photo" role="img" aria-label="Portrait photo of the therapist in a blue blazer outdoors"></div>
  <h2 class="about-name heading">Daniel Mercer, <span class="accent">LCSW</span></h2>
  <div class="rule" style="left:616px;top:2526px;width:143px"></div>
  <div class="about-copy">
    <p>Hi, I'm Daniel Mercer, a Licensed Psychotherapist and Clinical Social Worker in Denver, Colorado. I specialize in the treatment of Obsessive-Compulsive Disorder (OCD) and Anxiety Disorders.</p>
    <p>Generalized Anxiety Disorder, Social Anxiety Disorder, Panic Disorder, Health Anxiety, and Phobias. I have spent the last 10+ years guiding and empowering adults, teens, and children in overcoming these painful and difficult disorders.</p>
  </div>
  <div class="btn" style="left:618px;top:2754px;width:155px;height:44px;background:var(--sage);font-size:14px">Learn More <span class="dot"></span></div>
</section>

<!-- Contact -->
<section class="contact"></section>
<h2 class="sec-title heading" style="top:2978px">CONTACT <span class="accent">US</span></h2>
<div class="rule" style="left:540px;top:3032px;width:120px"></div>

<div class="info" style="left:224px">
  <svg width="48" height="50" viewBox="0 0 48 50"><path d="M24 4a12 12 0 0 0-12 12c0 9 12 20 12 20s12-11 12-20A12 12 0 0 0 24 4z" fill="none" stroke="#888" stroke-width="2"/><circle cx="24" cy="16" r="4" fill="none" stroke="#888" stroke-width="2"/><path d="M6 48l6-12h24l6 12z" fill="none" stroke="#888" stroke-width="2"/></svg>
  <div><b>LOCATION:</b><span>112 Aspen Hollow Drive Littleton,<br>CO 80120</span></div>
</div>
<div class="info" style="left:542px;top:3082px">
  <svg width="44" height="44" viewBox="0 0 44 44"><path d="M10 4l8 8-5 5c3 6 8 11 14 14l5-5 8 8-6 6C20 38 6 24 4 10z" fill="none" stroke="#888" stroke-width="2"/></svg>
  <div><b>PHONE:</b><span>303-555-0147</span></div>
</div>
<div class="info" style="left:765px;top:3082px">
  <svg width="50" height="40" viewBox="0 0 50 40"><rect x="2" y="4" width="46" height="32" fill="none" stroke="#888" stroke-width="2"/><path d="M2 4l23 18L48 4M2 36l17-16M48 36L31 20" fill="none" stroke="#888" stroke-width="2"/></svg>
  <div><b>EMAIL:</b><span>hello@quietharbor.com</span></div>
</div>

<p class="lead">Contact me with any questions. I'm happy to offer a free 30-minute online consultation.</p>
<div class="field" style="top:3263px">First Name</div>
<div class="field" style="top:3321px">Phone Number</div>
<div class="field" style="top:3380px">Email Address</div>
<div class="field" style="top:3436px;height:82px">Message</div>
<div class="submit">SUBMIT</div>
<div class="map" role="img" aria-label="Street map of the Littleton and Denver south suburbs with the office location pinned"></div>

<!-- Footer -->
<footer class="footer" role="img" aria-label="Faint Denver skyline behind the footer"></footer>
<div class="foot-brand"><span class="brand-mark"></span><div class="t"><b>Quiet Harbor</b><br>Daniel Mercer,LCSW</div></div>
<nav class="foot-nav"><span>Home</span><span>/</span><span>Therapy</span><span>/</span><span>OCD</span><span>/</span><span>Anxiety Disorders</span><span>/</span><span>About Daniel</span><span>/</span><span>Contact</span><span>/</span><span>Blog</span></nav>
<p class="copy">Copyright© 2024 <u>Quietharbor</u> | All Rights Reserved</p>
<div class="socials"><span></span><span></span><span></span><span></span></div>

</body>
</html>
```